Graphic Design Project

We make rose petal jelly from old fashioned english roses. The jelly is sweet eaten with scones and clotted cream or as a filling in a victoria sandwich, as a topping on ice cream or thick set yogurt.
The image of the product is luxurious and decadent and very english.
We need a design for a label which has a picture of an old fashioned rose (rosa mundi or a compte de chambard) The rose must stand out clearly so the jelly is not confused with other fruit jams. The overall colour of the label should be pink and soft, with white or dark pink writing. The label needs to be fridge proof.

We also need a security strip to fit on the lid of the jar.

We need the following information on the label.
Name of our company-"Petal Lantern"
Name of Product-"Rose Petal Jelly"
Sales pitch-"With whole petals-a taste of summer, delicious on scones, as a filling in sponge cake, as a topping on ice cream or yogurt."
INGREDIENTS: Sugar, water, rose petals, lemon juice, natural jelling agent (agar-agar)
STORAGE: Store in a cool dry place, once opened keep refrigerated and consume within 4 weeks.
BEST BEFORE: See base

200g
Produced by:
PETAL LANTERN
The Brambles
Marsh Lane
Ashcombe
Gloucestershire
GL19 4QT
The label must have room for a bar code. The size of label approx 8-10cm long 5cm wide.
Updates

Hi

Just been looking at the Greville and Hartley site and the labels they have there have the up market feel I am trying to convey. Hope that helps, its classy but not twee.

Thanks

Thanks for all submissions. I would be grateful if you googled images for 'Colourful and expensive biscuits at Greville Hartley' The designs on the tins are the image we are trying to create. The colours are quite strong.

Thanks

Target Market(s)

older well off people who visit garden centres

Industry/Entity Type

Security

Requirements
Must have
• All writen info above and picture of old fashioned rose prferably rose a mundi. Luxury feel, very english, to appeal to older market
Pink colour sheme
Should not have
• dark or manly colours

```html
<!DOCTYPE html>
<html lang="en">
<head>
<meta charset="utf-8">
<title>Petal Lantern – Rose Petal Jelly Label</title>
<link rel="stylesheet" href="https://fonts.googleapis.com/css2?family=Sorts+Mill+Goudy&display=swap">
<style>
  :root {
    --label-pink: #f8d5f4;
    --glow-white: #ffffff;
    --panel-white: #ffffff;
    --ink: #111111;
    --title-red: #ec1028;
    --rose-deep: #d9304f;
    --rose-mid: #f0607a;
    --frame-line: #222222;
  }
  html, body {
    margin: 0;
    padding: 0;
    overflow: hidden;
    background: var(--panel-white);
  }
  .label {
    position: relative;
    width: 1200px;
    height: 750px;
    overflow: hidden;
    font-family: "Sorts Mill Goudy", "Goudy Old Style", Georgia, serif;
    color: var(--ink);
  }
  .front {
    position: absolute;
    left: 0;
    top: 0;
    width: 797px;
    height: 750px;
    background:
      radial-gradient(circle at 400px 400px, var(--glow-white) 0, rgba(255,255,255,0.6) 120px, rgba(255,255,255,0) 250px),
      var(--label-pink);
    text-align: center;
  }
  .brand {
    position: absolute;
    left: 0;
    width: 810px;
    top: 40px;
    margin: 0;
    font-size: 54px;
    font-weight: 400;
    line-height: 1;
  }
  .product {
    position: absolute;
    left: 0;
    width: 818px;
    top: 118px;
    margin: 0;
    font-size: 72px;
    font-weight: 400;
    line-height: 1;
    color: var(--title-red);
  }
  .tagline {
    position: absolute;
    left: 0;
    width: 818px;
    top: 209px;
    margin: 0;
    font-size: 24px;
    line-height: 1.2;
  }
  .rose-art {
    position: absolute;
    left: 255px;
    top: 293px;
    width: 262px;
    height: 230px;
    border-radius: 48%;
    background: radial-gradient(circle at 50% 50%, var(--rose-mid) 0, var(--rose-deep) 70%, rgba(217,48,79,0) 100%);
  }
  .serving {
    position: absolute;
    left: 0;
    width: 826px;
    top: 588px;
    margin: 0;
    font-size: 31px;
    line-height: 42px;
  }
  .net-weight {
    position: absolute;
    left: 612px;
    top: 698px;
    margin: 0;
    font-size: 32px;
    line-height: 1;
  }
  .back {
    position: absolute;
    left: 797px;
    top: 0;
    width: 403px;
    height: 750px;
    background: var(--panel-white);
  }
  .info {
    position: absolute;
    left: 20px;
    margin: 0;
    font-size: 22px;
    line-height: 30px;
    width: 390px;
  }
  .info--ingredients { top: 28px; }
  .info--storage { top: 151px; }
  .info--best-before { top: 278px; }
  .producer {
    position: absolute;
    left: 22px;
    top: 378px;
    margin: 0;
    font-style: normal;
    font-size: 29px;
    line-height: 35px;
  }
  .barcode-space {
    position: absolute;
    left: 204px;
    top: 637px;
    width: 174px;
    height: 87px;
    border: 1.5px solid var(--frame-line);
    box-sizing: border-box;
    padding: 22px 0 0 7px;
    font-family: Arial, Helvetica, sans-serif;
    font-size: 18px;
    line-height: 24px;
  }
</style>
</head>
<body>
  <main class="label">
    <section class="front">
      <h1 class="brand">Petal Lantern</h1>
      <h2 class="product">Rose Petal Jelly</h2>
      <p class="tagline">"With whole petals its a taste of summer”</p>
      <div class="rose-art" role="img" aria-label="Illustration of three old fashioned pink roses"></div>
      <p class="serving">Delicious on scones, as a filling<br>in sponge cake, as a topping<br>on ice cream or yogurt."</p>
      <p class="net-weight">200g</p>
    </section>
    <section class="back">
      <p class="info info--ingredients">INGREDIENTS:<br>Sugar, water, rose petals, lemon<br>juice, natural jelling agent (agar-agar)</p>
      <p class="info info--storage">STORAGE: Store in a cool dry<br>place, once opened keep refrigerated<br>and consume within 4 weeks.</p>
      <p class="info info--best-before">BEST BEFORE:<br>See base</p>
      <address class="producer">Produced by:<br>PETAL LANTERN<br>The Brambles<br>Marsh Lane<br>Ashcombe<br>Gloucestershire<br>GL19 4QT</address>
      <div class="barcode-space">Bar<br>Code</div>
    </section>
  </main>
</body>
</html>
```